HIghly Competitive Dance School needs a web page make-over!!

Looking for a web design that captures our brand identity (Royal theme) that is New & Innovative and appeals to parents & children. I am open to creativity and want something original. Our color scheme is Burgundy & Gold with Black highlights. I currently use NetPerch and have up to 10 pages to publish.

Reason: I have run into some problems that have prevented me from making a selection; please bear with me.

Reason: To all the designers...I apologize for the delay but I am in the middle of fall registration and construction on a new building. I can return to this task on Monday but I am deep in the middle of back-to-school. Please forgive me for this very long delay. Thanks for your understanding!!

To all the designers...I apologize for the delay but I am in the middle of fall registration and construction on a new building. I can return to this task on Monday but I am deep in the middle of back-to-school. Please forgive me for this very long delay. Thanks for your understanding!!

Target Market(s)

Parents with young children who have a disposable income

Industry/Entity Type

School

Requirements
Must have
• Home Page
Classes
Policies/Guidelines
Our Staff (with pictures)
Contact Us (complete your info here)
Our Story (history page)
Gallery (pictures & Videos)
Registration Form (with coinloop feature)

```html
<!DOCTYPE html>
<html lang="en">
<head>
<meta charset="utf-8">
<title>Crownline Dance Studio — Home</title>
<link rel="stylesheet" href="https://fonts.googleapis.com/css2?family=Gelasio:wght@400;700&display=swap">
<style>
:root{
  --burgundy:#8b0019;
  --burgundy-dark:#5a0012;
  --button:#4e0010;
  --gold:#e8a93a;
  --orange:#e8612c;
  --ink:#1a1a1a;
  --panel:#f2f2f2;
  --sidebar:#e6e6e6;
  --white:#ffffff;
  --footer-text:#f1d9dd;
}
*{margin:0;padding:0;box-sizing:border-box}
html,body{width:1000px;height:1200px;overflow:hidden;background:var(--white)}
body{font-family:"Gelasio",Georgia,serif;color:var(--ink);position:relative}
.abs{position:absolute}
.intro{left:0;top:0;width:250px;height:350px;background:var(--panel)}
.brand{left:0;top:22px;width:250px;text-align:center;color:var(--burgundy)}
.brand-mark{display:inline-block;width:14px;height:14px;background:var(--burgundy);margin-bottom:4px}
.brand-name{font-size:30px;line-height:32px}
.brand-sub{font-size:11px;line-height:14px}
.tagline{left:28px;top:107px;font-size:10px;color:var(--burgundy);letter-spacing:.3px}
.intro-text{left:28px;top:132px;width:200px;font-size:13.5px;line-height:17px;color:var(--orange);text-align:justify}
.btn{display:block;background:var(--button);color:var(--white);font-size:12px;text-align:center;border-radius:9px;height:30px;line-height:30px;text-decoration:none;letter-spacing:.3px}
.apply{left:68px;top:280px;width:120px}
.hero{left:250px;top:0;width:750px;height:350px;background:linear-gradient(135deg,#3a2620 0%,#7a5c4c 35%,#c9b4a6 55%,#9a2b2b 80%,#4a1c18 100%)}
.dots{left:526px;top:318px;width:176px;height:20px;background:rgba(0,0,0,.35);border-radius:10px;display:flex;gap:9px;padding:4px 0 0 24px}
.dot{width:13px;height:13px;border-radius:50%;background:#d8d8d8}
.dot.active{background:#d0102a}
.nav{left:0;top:350px;width:1000px;height:100px;background:var(--burgundy)}
.nav-list{left:80px;top:0;display:flex;list-style:none}
.nav-item{width:120px;height:100px;color:var(--white);font-size:13.5px;line-height:16px;text-align:center;display:flex;flex-direction:column;align-items:center;justify-content:flex-end;padding-bottom:22px}
.nav-item.current{background:var(--burgundy-dark)}
.nav-item svg{margin-bottom:6px}
h2{font-weight:700;color:var(--burgundy)}
.welcome-title{left:20px;top:475px;font-size:22px}
.welcome-text{left:20px;top:516px;width:650px;font-size:13.5px;line-height:17px;text-align:justify}
.policies-title{left:20px;top:625px;font-size:22px}
.policies-text{left:20px;top:667px;width:300px;font-size:13.5px;line-height:17px;text-align:justify}
.subhead{color:var(--burgundy);font-size:13.5px;text-transform:uppercase;margin-top:16px}
.staff-title{left:370px;top:626px;font-size:18.5px}
.staff-list{left:370px;top:664px;list-style:none;font-size:13.5px;line-height:17px}
.staff-list li{margin-bottom:16px}
.read-policies{left:20px;top:883px;width:120px}
.read-staff{left:370px;top:862px;width:120px}
.photo-left{left:45px;top:915px;width:290px;height:135px;background:linear-gradient(180deg,#f4e6f4,#b86ab8)}
.photo-right{left:352px;top:915px;width:346px;height:135px;background:linear-gradient(180deg,#f7eef0,#8a2a40)}
.sidebar{left:700px;top:450px;width:300px;height:600px;background:var(--sidebar)}
.who-title{left:710px;top:486px;font-size:18.5px}
.bio-head{left:710px;top:529px;font-size:15.5px}
.bio-head span{color:var(--burgundy)}
.bio-photo{left:750px;top:555px;width:200px;height:258px;background:linear-gradient(160deg,#a9826a,#e7c9b4 50%,#c7a0b8)}
.bio-text{left:710px;top:826px;width:280px;font-size:13.5px;line-height:17px;text-align:justify}
.read-bio{left:790px;top:964px;width:120px}
.footer{left:0;top:1050px;width:1000px;height:150px;background:var(--burgundy)}
.address{left:93px;top:1095px;font-size:13.5px;line-height:17px;color:var(--footer-text)}
.copyright{right:14px;top:1158px;font-size:13.5px;color:var(--footer-text)}
</style>
</head>
<body>

<section class="abs intro"></section>
<div class="abs brand">
  <span class="brand-mark"></span>
  <div class="brand-name">Crownline</div>
  <div class="brand-sub">DANCE STUDIO, LLC</div>
</div>
<p class="abs tagline">BUILDING GENERATIONS OF DANCERS.</p>
<p class="abs intro-text">You asked for 'em. Boy, did we deliver. Our class schedule is brimming with good stuff. Whether you're a Ballerina or Tap Master, we have something to stretch your leotard!</p>
<a class="abs btn apply" href="#">APPLY NOW</a>

<div class="abs hero" role="img" aria-label="Stage photo of young ballet dancers in white and red tutus performing with a male dancer"></div>
<div class="abs dots"><span class="dot active"></span><span class="dot"></span><span class="dot"></span><span class="dot"></span><span class="dot"></span><span class="dot"></span></div>

<nav class="abs nav">
  <ul class="abs nav-list">
    <li class="nav-item current">
      <svg width="34" height="32" viewBox="0 0 34 32" fill="none" stroke="#fff" stroke-width="3"><path d="M3 16 L17 3 L31 16"/><path d="M7 13 V29 H14 V20 H20 V29 H27 V13"/></svg>Home</li>
    <li class="nav-item">
      <svg width="34" height="34" viewBox="0 0 34 34" fill="none" stroke="#fff" stroke-width="3"><circle cx="17" cy="19" r="12"/><path d="M17 12 V19 L22 22"/><path d="M4 8 L9 3 M30 8 L25 3"/></svg>Classes</li>
    <li class="nav-item">
      <svg width="34" height="36" viewBox="0 0 34 36" fill="none" stroke="#fff" stroke-width="2.5"><rect x="4" y="5" width="24" height="28"/><path d="M8 2 V8 M14 2 V8 M20 2 V8"/><path d="M10 20 L15 25 L31 9"/></svg>Policies<br>&amp; Guidelines</li>
    <li class="nav-item">
      <svg width="52" height="36" viewBox="0 0 52 36" fill="#fff" opacity=".9"><circle cx="10" cy="7" r="4"/><rect x="5" y="12" width="10" height="22" rx="3"/><circle cx="21" cy="6" r="4"/><rect x="16" y="11" width="10" height="23" rx="3"/><circle cx="32" cy="6" r="4"/><rect x="27" y="11" width="10" height="23" rx="3"/><circle cx="43" cy="7" r="4"/><rect x="38" y="12" width="10" height="22" rx="3"/></svg>Our Staff</li>
    <li class="nav-item">
      <svg width="72" height="36" viewBox="0 0 72 36" fill="none" stroke="#fff" stroke-width="2"><rect x="4" y="26" width="62" height="8" rx="2"/><rect x="8" y="17" width="58" height="8" rx="2"/><rect x="12" y="8" width="50" height="8" rx="2"/><rect x="20" y="1" width="34" height="6" rx="2"/></svg>Our Story</li>
    <li class="nav-item">
      <svg width="34" height="34" viewBox="0 0 34 34" fill="#fff"><circle cx="17" cy="17" r="15"/><circle cx="17" cy="8" r="4" fill="#8b0019"/><circle cx="17" cy="26" r="4" fill="#8b0019"/><circle cx="8" cy="17" r="4" fill="#8b0019"/><circle cx="26" cy="17" r="4" fill="#8b0019"/></svg>Gallery</li>
    <li class="nav-item">
      <svg width="48" height="34" viewBox="0 0 48 34" fill="none" stroke="#fff" stroke-width="3"><rect x="2" y="2" width="44" height="30"/><path d="M2 2 L24 20 L46 2 M2 32 L18 16 M46 32 L30 16"/></svg>Contact Us</li>
  </ul>
</nav>

<main>
  <h2 class="abs welcome-title">Greetings and Welcome</h2>
  <p class="abs welcome-text">Welcome to Crownline Dance Studio! We are so delighted to have you join our dance family and excited about the possibilities of what this year will bring. We are here to help in any way possible and to guide you through the process of the year. We strive to have an open door policy and we invite your comments, suggestions, concerns and even your criticism; as this is the only way we can address matters quickly and continue to bring you the service you deserve.</p>

  <h2 class="abs policies-title">Policies &amp; Guidelines</h2>
  <div class="abs policies-text">
    <p>We thank you for your patronage, as we know you have many choices and we are pleased you have selected Crownline Dance Studio to mentor your child’s dance education. Please take a moment to read further so that you have an idea of what to expect from your new Crownline dance family!</p>
    <p class="subhead">Class observation</p>
    <p>Parents are encouraged to visit classes the first week of the month to observe their child’s progress. After the first week of classes, we ask</p>
  </div>
  <a class="abs btn read-policies" href="#">READ MORE</a>

  <h2 class="abs staff-title">Our Amazing Crownline Staff</h2>
  <ul class="abs staff-list">
    <li>Marisol Greene Hartley<br>Founder/Executive Director</li>
    <li>Julian Reeves<br>Artistic Director</li>
    <li>Dana Whitfield<br>Modern &amp; Tumbling</li>
    <li>Dr. Nkechi Adeyemi<br>Classical Ballet &amp; Pointe</li>
  </ul>
  <a class="abs btn read-staff" href="#">READ MORE</a>

  <div class="abs photo-left" role="img" aria-label="Group of young hip-hop dancers in purple outfits posing"></div>
  <div class="abs photo-right" role="img" aria-label="Young ballerinas in burgundy tutus posing in a line"></div>
</main>

<aside class="abs sidebar"></aside>
<h2 class="abs who-title">Who We Are</h2>
<p class="abs bio-head"><span>Marisol Greene Hartley</span>, Biography</p>
<div class="abs bio-photo" role="img" aria-label="Portrait of the studio founder with a young student"></div>
<p class="abs bio-text">Marisol Greene Hartley, B.A., M.S., completed her Bachelors Degree at Briarwood College in Briarwood, MI and later pursued her Master’s Degree at Ridgemont University of Pennsylvania. She began studying dance at age 8 in Detroit under the direction and tutelage of Loretta M. Banks at Eastgate School of</p>
<a class="abs btn read-bio" href="#">READ MORE</a>

<footer class="abs footer">
  <svg class="abs" style="left:68px;top:0" width="100" height="126" viewBox="0 0 100 126" fill="none" stroke="#cfcfcf" stroke-width="5"><path d="M42 2 L12 32 V123 H98"/></svg>
</footer>
<address class="abs address" style="font-style:normal">The Sterling Plaza<br>41820 Meadowbrook Hwy<br>&nbsp;Lakeview<br>Mi 48090 (Next door to Brothy's!)</address>
<p class="abs copyright">Content copyright 2013. Crownline Dance Studio, LLC. All rights reserved.</p>

</body>
</html>
```